Pelin Thai Massage Double Sided Flyer Luxury

I require a double sided flyer
we are a Thai Massage Spa
Would like gold, deep purple and bronze colours
Something eye catching and looks professional

```html
<!DOCTYPE html>
<html lang="en">
<head>
<meta charset="utf-8">
<title>Pelin Thai Massage – Flyer</title>
<link href="https://fonts.googleapis.com/css2?family=Philosopher:wght@400;700&family=Crimson+Text:wght@400;600&display=swap" rel="stylesheet">
<style>
  :root{
    --backdrop:#3b3b3d;
    --bronze-deep:#2a160e;
    --bronze-mid:#3a2015;
    --gold-light:#fcc53a;
    --gold:#f0a91c;
    --gold-dark:#d98a0c;
    --ink:#2a1608;
    --cream:#fdf3e0;
    --frame:#ffffff;
  }
  *{box-sizing:border-box;margin:0;padding:0}
  html,body{width:1200px;height:776px;overflow:hidden;background:var(--backdrop)}
  .canvas{position:relative;width:1200px;height:776px}
  .flyer{
    position:absolute;top:38px;width:495px;height:700px;
    background:radial-gradient(ellipse at 50% 30%,var(--bronze-mid),var(--bronze-deep) 75%);
    box-shadow:0 10px 28px rgba(0,0,0,.45);overflow:hidden;
  }
  .flyer--front{left:80px}
  .flyer--back{left:625px}
  .gold-band{
    position:absolute;left:0;right:0;
    background:linear-gradient(180deg,var(--gold-light),var(--gold) 55%,var(--gold-dark));
    color:var(--ink);text-align:center;
  }
  .photo{
    position:absolute;border:3px solid var(--frame);
  }
  .photo--full{border:none}
  /* front */
  .brand{position:absolute;top:52px;left:0;right:0;text-align:center}
  .brand-dot{width:14px;height:14px;border-radius:50%;background:var(--gold);margin:0 auto 16px}
  .brand-name{font-family:'Philosopher',sans-serif;font-size:31px;color:var(--gold);letter-spacing:.5px}
  .welcome{top:168px;height:152px;padding:18px 34px 0}
  .welcome h2{font-family:'Philosopher',sans-serif;font-weight:400;font-size:20px;margin-bottom:10px}
  .welcome p{font-family:'Crimson Text',serif;font-size:12.5px;line-height:1.25;margin-bottom:10px}
  .contact{
    position:absolute;left:0;right:0;text-align:center;
    font-family:'Philosopher',sans-serif;color:var(--cream);font-size:19px;line-height:1.35;
  }
  /* back */
  .intro{top:150px;height:96px;padding:16px 40px 0}
  .intro h3{font-family:'Philosopher',sans-serif;font-weight:400;font-size:16px;margin-bottom:6px;letter-spacing:.5px}
  .intro p{font-family:'Crimson Text',serif;font-size:14.5px;line-height:1.2}
  .section-title{
    position:absolute;top:254px;left:30px;right:30px;height:40px;
    border-top:2px solid var(--gold);border-left:2px solid var(--gold);border-right:2px solid var(--gold);
  }
  .section-title span{
    position:absolute;left:50%;top:-16px;transform:translateX(-50%);
    background:var(--bronze-mid);padding:0 12px;
    font-family:'Philosopher',sans-serif;font-size:24px;color:var(--gold);white-space:nowrap;
  }
  .price-list{position:absolute;top:282px;left:28px;right:28px;display:flex;gap:10px}
  .price-card{
    flex:1;height:138px;padding:14px 10px 0;text-align:center;color:var(--ink);
    background:linear-gradient(180deg,var(--gold-light),var(--gold) 60%,var(--gold-dark));
  }
  .price-card h4{font-family:'Philosopher',sans-serif;font-weight:400;font-size:11px;text-transform:uppercase;line-height:1.1;min-height:26px}
  .price-card .price{
    font-family:'Philosopher',sans-serif;font-size:20px;line-height:1.1;
    border-top:1.5px solid var(--ink);border-bottom:1.5px solid var(--ink);margin:6px 4px;padding:4px 0;
  }
  .price-card p{font-family:'Crimson Text',serif;font-size:9.5px;line-height:1.15}
</style>
</head>
<body>
<main class="canvas">

  <section class="flyer flyer--front" aria-label="Flyer front">
    <div class="brand">
      <div class="brand-dot"></div>
      <div class="brand-name">Pelin Thai Massage</div>
    </div>

    <div class="gold-band welcome">
      <h2>Welcome to Luxury</h2>
      <p>Set in the heart of Oakwood, Pelin Thai Massage will allow you to immerse yourself in a place where your wellbeing and rejuvenation is at the centre of what we do.</p>
      <p>Using Thai traditions, our highly trained therapists offer revitalising body treatments with their deep tissue massage techniques. In their hands, you will see and feel immediate results.</p>
    </div>

    <div class="photo photo--full" role="img" aria-label="Photo of a woman receiving a back massage on a woven mat with spa candles"
         style="top:320px;left:0;width:495px;height:180px;background:linear-gradient(100deg,#e9e4dc 0%,#b9784a 35%,#c98d5e 60%,#8a4a2c 85%,#5b2e1c 100%)"></div>

    <div class="photo" role="img" aria-label="Photo of a relaxed woman receiving a shoulder massage"
         style="top:510px;left:28px;width:210px;height:112px;background:linear-gradient(110deg,#7a3b1c,#c37a4a 50%,#e6c9a8)"></div>
    <div class="photo" role="img" aria-label="Photo of spa items: purple bath salts, candle, oil bottle and towel"
         style="top:500px;left:248px;width:222px;height:112px;background:linear-gradient(110deg,#9c6bb8,#d9a36a 45%,#7d3a8c 80%,#c9a07a)"></div>

    <div class="contact" style="top:628px">42 Willow Row, Leeds, LS7 2QT<br>0113 496 0718 | www.pelinthaispa.co.uk</div>
  </section>

  <section class="flyer flyer--back" aria-label="Flyer back">
    <div class="photo" role="img" aria-label="Photo of a woman with a towel wrap receiving a facial massage"
         style="top:24px;left:28px;width:210px;height:100px;background:linear-gradient(110deg,#b98a5e,#e8cbb0 50%,#8a5a34)"></div>
    <div class="photo" role="img" aria-label="Photo of a woman with a flower in her hair receiving a back massage"
         style="top:20px;left:246px;width:222px;height:100px;background:linear-gradient(110deg,#c79a6c,#e9e2d8 35%,#8c4c2a 75%,#6b3a22)"></div>

    <div class="gold-band intro">
      <h3>MASSAGES</h3>
      <p>Restore balance. Revive your senses. Discover all the ways Pelin Thai Massage can breathe new life into your body and soul.</p>
    </div>

    <div class="section-title"><span>MASSAGES</span></div>

    <div class="price-list">
      <div class="price-card">
        <h4>Deep Tissue<br>Massage</h4>
        <div class="price">60 minutes<br>£45</div>
        <p>Oil massage personalised,<br>light to firm pressure</p>
      </div>
      <div class="price-card">
        <h4>Deep Tissue<br>Massage</h4>
        <div class="price">90 minutes<br>£55</div>
        <p>Oil massage, medium<br>to firm pressure</p>
      </div>
      <div class="price-card">
        <h4>Thai Floor Traditional<br>Massage</h4>
        <div class="price">60 minutes<br>£45</div>
        <p>Dry massage, medium to firm pressure<br>applying stretching technique</p>
      </div>
    </div>

    <div class="photo" role="img" aria-label="Photo of a woman resting during a shoulder massage"
         style="top:446px;left:28px;width:220px;height:118px;background:linear-gradient(110deg,#6e3418,#c07a48 50%,#e3bf98)"></div>
    <div class="photo" role="img" aria-label="Photo of hands massaging a back with warm stones"
         style="top:436px;left:256px;width:212px;height:118px;background:linear-gradient(110deg,#f1e3d4,#e0b08a 45%,#d39a70 75%,#f4ece4)"></div>

    <div class="contact" style="top:590px">42 Willow Row, Leeds, LS7 2QT<br>0113 496 0718 | www.pelinthaispa.co.uk</div>
  </section>

</main>
</body>
</html>
```